Anzeigengestaltung für Zahnarztpraxis
Zielgruppe
Wir sind eine Zahnarztpraxis in einer ländlichen Gemeinde mit 5000 Einwohnern in der Schweiz und bieten alles, was eine moderne Zahnarztpraxis zu bieten hat: Kieferorthopädie, allgemeine Zahnmedizin, Implantologie (schablonengeführt und digital geplant, Klarobeta, Intraoralscanner, 3D-Röntgen
Online-Agenda
Zielgruppe: 4-99
2023: 20 jähriges Jubiläum
Der Text sollte später leicht und von uns selbständig geändert werden können:
z.B.
Frühjahrsputz: 20 Franken Rabatt auf die nächste Prophylaxesitzung
Aktion im April: 20% Rabatt auf Klarobeta
Aktion im Mai 20% Rabatt auf Implantatbehandlungen
Sommeraktion Bleaching 495.-
Aufgabenstellung
Maße: 185x63mm, (185x130) beide quer
druckoptimiertes PDF X/-4
Bildauflösung: CMYK- und Graustufenbilder 300dpi
Farbprofil: PSOuncoated v3

```html
<!DOCTYPE html>
<html lang="de">
<head>
<meta charset="utf-8">
<title>Sommeraktion Bleaching – Anzeigen</title>
<link href="https://fonts.googleapis.com/css2?family=Ubuntu:wght@400;500;700&display=swap" rel="stylesheet">
<style>
  :root {
    --green: #80bb2c;
    --green-deep: #72b022;
    --green-text: #6aaa1c;
    --white: #ffffff;
    --canvas: #ffffff;
    --url-dark: #3d5a1a;
    --url-grey: #6b6b6b;
    --photo-hair: #a8733e;
    --photo-skin: #e2b294;
    --photo-leaf: #8fb26a;
    --photo-light: #f1e7dc;
  }
  * { margin: 0; padding: 0; box-sizing: border-box; }
  html, body { width: 1010px; height: 1200px; overflow: hidden; background: var(--canvas); }
  body { position: relative; font-family: "Ubuntu", sans-serif; }

  .ad {
    position: absolute;
    left: 135px;
    width: 750px;
    overflow: hidden;
    box-shadow: 0 14px 30px rgba(0,0,0,0.16);
  }
  .ad--large { top: 140px; height: 527px; }
  .ad--banner { top: 784px; height: 255px; }

  .ad__panel {
    position: absolute; top: 0; left: 0; height: 100%;
    background: linear-gradient(160deg, var(--green) 0%, var(--green-deep) 60%, var(--green) 100%);
  }
  .ad--large .ad__panel { width: 402px; }
  .ad--banner .ad__panel { width: 442px; }

  .ad__photo {
    position: absolute; top: 0; right: 0; height: 100%;
    background:
      radial-gradient(ellipse at 30% 25%, var(--photo-hair) 0%, transparent 45%),
      radial-gradient(ellipse at 80% 40%, var(--photo-light) 0%, transparent 50%),
      radial-gradient(ellipse at 45% 60%, var(--photo-skin) 0%, transparent 55%),
      linear-gradient(180deg, var(--photo-leaf) 0%, var(--photo-skin) 55%, var(--photo-light) 100%);
  }
  .ad--large .ad__photo { width: 348px; }
  .ad--banner .ad__photo { width: 308px; }

  .script-title {
    position: absolute;
    border-radius: 6px;
    background: rgba(255,255,255,0.18);
  }
  .ad--large .script-title { left: 132px; top: 69px; width: 258px; height: 41px; }
  .ad--banner .script-title { left: 260px; top: 26px; width: 167px; height: 27px; }

  .price {
    position: absolute;
    font-weight: 500;
    line-height: 1;
    letter-spacing: -2px;
    color: transparent;
    -webkit-text-stroke: 2px var(--white);
    white-space: nowrap;
  }
  .ad--large .price { left: 44px; top: 118px; font-size: 146px; }
  .ad--banner .price { left: 101px; top: 50px; font-size: 128px; }

  .service-box {
    position: absolute;
    background: var(--white);
    color: var(--green-text);
    font-weight: 700;
    letter-spacing: 1px;
    display: flex; align-items: center; justify-content: center;
  }
  .ad--large .service-box { left: 22px; top: 246px; width: 357px; height: 71px; font-size: 31px; }
  .ad--banner .service-box { left: 80px; top: 162px; width: 286px; height: 71px; font-size: 31px; }

  .brand { position: absolute; display: flex; align-items: center; color: var(--white); }
  .brand__dot { border-radius: 50%; background: var(--white); flex: none; }
  .brand__name { line-height: 1.05; font-weight: 500; }
  .ad--large .brand { left: 87px; top: 398px; }
  .ad--large .brand__dot { width: 58px; height: 58px; margin-right: 13px; }
  .ad--large .brand__name { font-size: 29px; }
  .ad--banner .brand { left: 18px; top: 21px; }
  .ad--banner .brand__dot { width: 34px; height: 34px; margin-right: 7px; }
  .ad--banner .brand__name { font-size: 17px; }

  .url { position: absolute; white-space: nowrap; }
  .ad--large .url { left: 158px; top: 472px; font-size: 12.5px; color: var(--url-dark); }
  .ad--banner .url { right: 20px; top: 222px; font-size: 9px; color: var(--url-grey); }

  .jubilee {
    position: absolute;
    color: var(--white);
    font-weight: 700;
    text-align: right;
    line-height: 1.12;
    text-shadow: 0 1px 4px rgba(0,0,0,0.35);
  }
  .ad--large .jubilee { right: 34px; top: 396px; font-size: 37px; }
  .ad--banner .jubilee { right: 25px; top: 19px; font-size: 29px; }

  .balloon {
    position: absolute; left: 197px; top: 25px; width: 51px; height: 46px;
    border-radius: 50% 50% 45% 45%;
    background: radial-gradient(circle at 35% 30%, #ffffff 0%, #e6e6e6 70%, #cfcfcf 100%);
  }
  .balloon-string {
    position: absolute; left: 222px; top: 71px; width: 1px; height: 90px;
    background: rgba(255,255,255,0.6);
  }
</style>
</head>
<body>

  <section class="ad ad--large" aria-label="Anzeige Sommeraktion, 185 × 130 mm">
    <div class="ad__panel"></div>
    <div class="ad__photo" role="img" aria-label="Foto: zwei lächelnde junge Frauen im Grünen"></div>
    <div class="script-title" role="img" aria-label="Handschriftzug: Sommeraktion"></div>
    <div class="price">495.-</div>
    <div class="service-box">BLEACHING</div>
    <div class="brand">
      <span class="brand__dot"></span>
      <span class="brand__name">Praxis Brunner<br>Zahnärzte</span>
    </div>
    <div class="url">www.praxisbrunner.ch</div>
    <div class="jubilee">Wir feiern<br>20 Jahre!</div>
  </section>

  <section class="ad ad--banner" aria-label="Anzeige Sommeraktion, 185 × 63 mm">
    <div class="ad__panel"></div>
    <div class="ad__photo" role="img" aria-label="Foto: zwei lächelnde junge Frauen im Grünen"></div>
    <div class="brand">
      <span class="brand__dot"></span>
      <span class="brand__name">Praxis Brunner<br>Zahnärzte</span>
    </div>
    <div class="balloon-string"></div>
    <div class="balloon" role="img" aria-label="Weisser Herzballon"></div>
    <div class="script-title" role="img" aria-label="Handschriftzug: Sommeraktion"></div>
    <div class="price">495.-</div>
    <div class="service-box">BLEACHING</div>
    <div class="jubilee">Wir feiern<br>20 Jahre!</div>
    <div class="url">www.praxisbrunner.ch</div>
  </section>

</body>
</html>
```